Visitenkarten-Design für Fotograf gesucht
Zielgruppe
Ich bin Fotograf der ein step in Richtung Professionalität wagen möchte.
Aufgabenstellung
Ich habe bereits ein Logo welches ich als Datei angefügt habe.
Ich hatte überlegt gehabt eine Art Prägung im Design zu haben bzw. in der Visitenkarte, eventuell das Kamera Zeichen in meinem Logo. Sonst bin ich relativ offen.
Eine weitere Überlegung ist eine eher kontrastreiche Karte haben könnte, eventuell die Rückseite dunkelgrau oder schwarz.
Es kann wenn man eine dritte Farbe hinzufügen möchte ein mittleres bis dunkles Rot hinzufügen.
Ich habe ein paar Designs hinzugefügt die mir sehr zugesagt haben.
Ansonsten bin ich auch für ein Design in der kompletten Gegenteiligkeit offen.

```html
<!DOCTYPE html>
<html lang="de">
<head>
<meta charset="utf-8">
<title>Mirko Trell Photography – Visitenkarte</title>
<link rel="stylesheet" href="https://fonts.googleapis.com/css2?family=Open+Sans:wght@400;600&display=swap">
<style>
  :root {
    --stage: #e4e3e2;
    --paper: #ffffff;
    --charcoal: #57524f;
    --charcoal-line: #6b6562;
    --ink: #2b2929;
    --text: #3d3a39;
    --red: #b5363a;
    --red-line: #d0494c;
  }
  * { box-sizing: border-box; margin: 0; padding: 0; }
  html, body {
    width: 1200px; height: 800px; overflow: hidden;
    background: var(--stage);
    font-family: "Open Sans", Arial, sans-serif;
    color: var(--text);
  }
  .stage {
    position: relative; width: 1200px; height: 800px;
    display: flex; align-items: center; justify-content: center; gap: 60px;
  }
  .card {
    position: relative; width: 520px; height: 336px;
    box-shadow: 0 10px 30px rgba(0,0,0,.18);
    overflow: hidden;
  }

  /* front */
  .card--front { background: var(--paper); }
  .brand {
    position: absolute; left: 36px; top: 46px;
    display: flex; flex-direction: column; align-items: flex-end;
  }
  .brand__name {
    font-size: 34px; font-weight: 600; color: var(--ink); line-height: 1;
  }
  .brand__tag {
    margin-top: 6px; font-size: 9px; font-weight: 600; letter-spacing: 3px; color: var(--ink);
  }
  .band-rule {
    position: absolute; left: 0; right: 0; top: 118px; height: 1px; background: var(--charcoal);
  }
  .band {
    position: absolute; left: 0; right: 0; top: 124px; height: 68px; background: var(--charcoal);
  }
  .band-rule--red {
    position: absolute; left: 0; right: 0; top: 200px; height: 3px; background: var(--red-line);
  }
  .marker { position: absolute; top: 140px; width: 30px; height: 44px; }
  .marker--phone { left: 80px; }
  .marker--mail { left: 245px; }
  .marker--pin { left: 410px; }
  .contact {
    position: absolute; font-size: 15px; line-height: 1.3; color: var(--text);
  }
  .contact--phone { left: 60px; top: 232px; }
  .contact--web { left: 190px; top: 232px; }
  .contact--address { right: 36px; top: 232px; text-align: right; }
  .base-rule {
    position: absolute; left: 0; right: 0; bottom: 22px; height: 3px; background: var(--red-line);
  }

  /* back */
  .card--back { background: var(--charcoal); }
  .back-brand {
    position: absolute; inset: 0;
    display: flex; flex-direction: column; align-items: center; justify-content: center;
  }
  .back-brand__name {
    font-size: 54px; font-weight: 600; color: var(--ink); line-height: 1;
  }
  .back-brand__tag {
    margin-top: 10px; margin-left: 150px;
    font-size: 12px; font-weight: 600; letter-spacing: 4px; color: var(--ink);
  }
</style>
</head>
<body>
<main class="stage">
  <section class="card card--front" aria-label="Vorderseite">
    <div class="brand">
      <span class="brand__name">Mirko Trell</span>
      <span class="brand__tag">PHOTOGRAPHY</span>
    </div>

    <div class="band-rule"></div>
    <div class="band"></div>
    <div class="band-rule--red"></div>

    <svg class="marker marker--phone" viewBox="0 0 30 44" aria-hidden="true">
      <path d="M15 44 L9 28 L21 28 Z" fill="var(--charcoal)"/>
      <circle cx="15" cy="15" r="14" fill="var(--red)"/>
      <path d="M10 9c1-1 2-1 3 0l1 2c0 1-1 1-1 2 1 2 2 3 4 4 1 0 1-1 2-1l2 1c1 1 1 2 0 3-1 1-2 2-4 1-3-1-6-4-7-7-1-2 0-4 0-5z" fill="#fff"/>
    </svg>
    <svg class="marker marker--mail" viewBox="0 0 30 44" aria-hidden="true">
      <path d="M15 44 L9 28 L21 28 Z" fill="var(--charcoal)"/>
      <circle cx="15" cy="15" r="14" fill="var(--red)"/>
      <rect x="8" y="10" width="14" height="10" fill="#fff"/>
      <path d="M8 10 L15 16 L22 10" fill="none" stroke="var(--red)" stroke-width="1.2"/>
    </svg>
    <svg class="marker marker--pin" viewBox="0 0 30 44" aria-hidden="true">
      <path d="M15 44 L9 28 L21 28 Z" fill="var(--charcoal)"/>
      <circle cx="15" cy="15" r="14" fill="var(--red)"/>
      <path d="M15 23c-3-4-5-6-5-9a5 5 0 0 1 10 0c0 3-2 5-5 9z" fill="#fff"/>
      <circle cx="15" cy="14" r="2" fill="var(--red)"/>
    </svg>

    <p class="contact contact--phone">+49 123 456<br>+49 123 789</p>
    <p class="contact contact--web">www.mt-photography.de</p>
    <p class="contact contact--address">musterstraße 1<br>1234 musterstadt</p>

    <div class="base-rule"></div>
  </section>

  <section class="card card--back" aria-label="Rückseite">
    <div class="back-brand">
      <span class="back-brand__name">Mirko Trell</span>
      <span class="back-brand__tag">PHOTOGRAPHY</span>
    </div>
  </section>
</main>
</body>
</html>
```